Business card for technical support company.
FixWiseDesk.com
Business card for technical support company.  - Computers
Creative Brief
Use specific fonts
Up To designer
Professional
Marcus Bell
VP In Charge
482 Alder Lane New York, NY 48213
service@FixWiseDesk.com
This will be used as a mock-up for my business card. Editable Adobe Illustrator or comparable original design file will need to be included with the final design. Also logo can be broken up from the FixWiseDesk.com below it and arranged on the card.
Company logo, website, and possible list of services. Please allow room to add later. 5-6 bullet points
qm71xrb qm71xrb
Nice first drafts everyone. I would like to see how some of these look with a white background instead of black. Nice!
I would like one design but two separate color schemes. Please match the two color schemes of the example logos provided. Thank you!

```html
<!DOCTYPE html>
<html lang="en">
<head>
<meta charset="utf-8">
<title>FixWiseDesk Business Card</title>
<link rel="stylesheet" href="https://fonts.googleapis.com/css2?family=Open+Sans:wght@400;600;700&display=swap">
<style>
  :root {
    --bg: #dcdcde;
    --card-white: #ffffff;
    --card-dark: #2c2c2f;
    --card-dark-2: #3a3a3e;
    --stripe: #e8eaee;
    --blue: #1e6fd9;
    --blue-deep: #0d3f9e;
    --blue-light: #3a9bf0;
    --white: #ffffff;
    --muted: #c9ccd4;
  }
  * { margin: 0; padding: 0; box-sizing: border-box; }
  html, body { width: 1200px; height: 902px; overflow: hidden; }
  body {
    background: var(--bg);
    font-family: "Open Sans", Arial, sans-serif;
    position: relative;
  }
  .card {
    position: absolute;
    width: 620px;
    height: 354px;
    border-radius: 4px;
    overflow: hidden;
    box-shadow: 0 10px 24px rgba(0,0,0,0.18);
  }
  .card-front {
    left: 400px; top: 64px;
    background: var(--card-white);
    display: flex; align-items: center; justify-content: center;
  }
  .brand { display: flex; align-items: center; gap: 12px; }
  .brand-mark { width: 26px; height: 26px; background: var(--blue); }
  .brand-name {
    font-weight: 700; font-size: 30px; color: var(--blue);
    letter-spacing: 0.5px;
  }
  .card-back {
    left: 180px; top: 484px;
    background: var(--card-dark);
  }
  .card-back .wave { position: absolute; inset: 0; }
  .card-back .brand { position: absolute; left: 34px; top: 40px; }
  .card-back .brand-mark { width: 20px; height: 20px; background: var(--blue-light); }
  .card-back .brand-name { font-size: 22px; color: var(--white); }
  .person { position: absolute; left: 34px; bottom: 50px; color: var(--white); }
  .person-name { font-weight: 700; font-size: 19px; }
  .person-role { font-size: 14px; margin-top: 2px; color: var(--muted); }
  .contact {
    position: absolute; right: 30px; top: 58px;
    list-style: none; text-align: right;
    color: var(--white); font-size: 12px; line-height: 20px;
  }
  .contact li { display: flex; justify-content: flex-end; align-items: center; gap: 7px; }
  .contact svg { width: 10px; height: 10px; fill: var(--white); flex: none; }
</style>
</head>
<body>
  <section class="card card-front">
    <div class="brand">
      <span class="brand-mark"></span>
      <span class="brand-name">FixWiseDesk</span>
    </div>
  </section>

  <section class="card card-back">
    <svg class="wave" viewBox="0 0 620 354" preserveAspectRatio="none" aria-hidden="true">
      <defs>
        <linearGradient id="blueSweep" x1="0" y1="1" x2="1" y2="0">
          <stop offset="0" stop-color="#0d3f9e"/>
          <stop offset="0.55" stop-color="#1e6fd9"/>
          <stop offset="1" stop-color="#3a9bf0"/>
        </linearGradient>
      </defs>
      <path d="M0 354 L0 320 C160 320 230 270 282 196 C320 130 360 20 620 -14 L620 354 Z" fill="#3a3a3e"/>
      <path d="M40 354 C190 342 250 294 300 212 C336 142 374 30 620 4 L620 354 Z" fill="#e8eaee"/>
      <path d="M60 354 C205 344 264 300 312 222 C346 150 386 42 620 16 L620 354 Z" fill="url(#blueSweep)"/>
    </svg>

    <div class="brand">
      <span class="brand-mark"></span>
      <span class="brand-name">FixWiseDesk</span>
    </div>

    <ul class="contact">
      <li>214 Birch Road Mall <svg viewBox="0 0 10 10"><path d="M5 0a3.5 3.5 0 0 0-3.5 3.5C1.5 6 5 10 5 10s3.5-4 3.5-6.5A3.5 3.5 0 0 0 5 0z"/></svg></li>
      <li>Cedar Row Road 4KT <svg viewBox="0 0 10 10"><path d="M5 0a3.5 3.5 0 0 0-3.5 3.5C1.5 6 5 10 5 10s3.5-4 3.5-6.5A3.5 3.5 0 0 0 5 0z"/></svg></li>
      <li>018 462 3071 <svg viewBox="0 0 10 10"><path d="M2 0l2 2.5-1 1.3a6 6 0 0 0 3.2 3.2l1.3-1L10 8l-1.5 2C4 10 0 6 0 1.5z"/></svg></li>
      <li>018 462 3071 <svg viewBox="0 0 10 10"><rect x="2" y="0" width="6" height="10" rx="1"/></svg></li>
      <li>dl.hart@email.com <svg viewBox="0 0 10 10"><path d="M0 2h10v6H0z"/></svg></li>
      <li>www.fixwisedesk.com <svg viewBox="0 0 10 10"><circle cx="5" cy="5" r="5"/></svg></li>
    </ul>

    <div class="person">
      <div class="person-name">Dana Lowe-Hart</div>
      <div class="person-role">Consultant</div>
    </div>
  </section>
</body>
</html>
```